依頼概要
初めまして。よろしくお願いいたします。

依頼内容
※エコー(赤ちゃん)ポスターのデザイン依頼

※エコー写真をスキャンして嵌め込みますので、そちらを想定したテンプレート型のポスターデザインをお願いいたします。

※エコーの枚数は3・6・9枚の何れかでお願いいたします。

※子供の名前 身長体重 出産時間 等

ポスターデザインのイメージや雰囲気は
デザイナー様各々におまかせしております。

```html
<!DOCTYPE html>
<html lang="ja">
<head>
<meta charset="utf-8">
<title>太郎 エコーポスター</title>
<link href="https://fonts.googleapis.com/css2?family=Noto+Serif+JP:wght@500&family=Noto+Sans+JP:wght@400&display=swap" rel="stylesheet">
<style>
  :root {
    --sky: #c6ddf3;
    --sky-deep: #b6d1ed;
    --frame: #ffffff;
    --ink: #1d1d1d;
    --leaf: #7dbb3a;
    --leaf-light: #c9e59a;
    --scan-dark: #0b0b0b;
    --scan-mid: #4a4a4a;
  }
  html, body {
    margin: 0;
    padding: 0;
    overflow: hidden;
  }
  .poster {
    position: relative;
    width: 846px;
    height: 1200px;
    background: linear-gradient(180deg, var(--sky) 0%, var(--sky-deep) 100%);
    overflow: hidden;
  }
  .poster-frame {
    position: absolute;
    inset: 20px 28px 20px 28px;
    border: 2px solid var(--frame);
    pointer-events: none;
  }
  .vine-corner {
    position: absolute;
    left: 0;
    top: 0;
    width: 310px;
    height: 290px;
  }
  .flower-corner {
    position: absolute;
    right: 0;
    bottom: 0;
    width: 360px;
    height: 360px;
  }
  .baby-name {
    position: absolute;
    top: 44px;
    left: 0;
    width: 100%;
    margin: 0;
    text-align: center;
    font-family: "Noto Serif JP", serif;
    font-weight: 500;
    font-size: 54px;
    line-height: 80px;
    letter-spacing: 6px;
    color: var(--ink);
  }
  .birth-details {
    position: absolute;
    top: 136px;
    left: 96px;
    width: 660px;
    margin: 0;
    display: flex;
    justify-content: space-between;
    font-family: "Noto Sans JP", sans-serif;
    font-size: 23px;
    line-height: 34px;
    color: var(--ink);
  }
  .scan-grid {
    position: absolute;
    left: 85px;
    top: 185px;
    width: 700px;
    display: grid;
    grid-template-columns: 338px 338px;
    column-gap: 24px;
    row-gap: 30px;
  }
  .scan-card { margin: 0; }
  .scan-photo {
    width: 338px;
    height: 248px;
    background: radial-gradient(ellipse at 50% 55%, var(--scan-mid) 0%, var(--scan-dark) 70%);
  }
  .scan-date {
    margin-top: 12px;
    font-family: "Noto Sans JP", sans-serif;
    font-size: 16px;
    line-height: 22px;
    color: var(--ink);
    white-space: nowrap;
  }
</style>
</head>
<body>
  <main class="poster">
    <div class="poster-frame"></div>

    <svg class="vine-corner" viewBox="0 0 310 290" role="img" aria-label="緑の葉と白い花のつるの飾り">
      <defs>
        <linearGradient id="vine-tone" x1="0" y1="0" x2="1" y2="1">
          <stop offset="0" stop-color="var(--leaf)"/>
          <stop offset="1" stop-color="var(--leaf-light)" stop-opacity="0.6"/>
        </linearGradient>
      </defs>
      <path d="M0 0 H305 Q300 30 250 34 Q150 40 95 45 Q55 52 50 100 Q46 180 40 250 Q36 282 20 290 H0 Z" fill="url(#vine-tone)"/>
    </svg>

    <svg class="flower-corner" viewBox="0 0 360 360" role="img" aria-label="白い花と緑の葉のつるの飾り">
      <defs>
        <linearGradient id="flower-tone" x1="1" y1="1" x2="0" y2="0">
          <stop offset="0" stop-color="var(--leaf)"/>
          <stop offset="1" stop-color="var(--leaf-light)" stop-opacity="0.6"/>
        </linearGradient>
      </defs>
      <path d="M360 0 V360 H0 Q10 330 60 326 Q180 318 265 312 Q305 306 310 260 Q314 160 322 60 Q326 12 360 0 Z" fill="url(#flower-tone)"/>
    </svg>

    <h1 class="baby-name">太郎</h1>
    <p class="birth-details"><span>誕生：○○時○○分</span><span>身長：○○cm</span><span>体重：○○g</span></p>

    <section class="scan-grid">
      <figure class="scan-card">
        <div class="scan-photo" role="img" aria-label="エコー写真 1枚目"></div>
        <figcaption class="scan-date">2020 年　○○月 ○○日 ○○時 ○○分</figcaption>
      </figure>
      <figure class="scan-card">
        <div class="scan-photo" role="img" aria-label="エコー写真 2枚目"></div>
        <figcaption class="scan-date">2020 年　○○月 ○○日 ○○時 ○○分</figcaption>
      </figure>
      <figure class="scan-card">
        <div class="scan-photo" role="img" aria-label="エコー写真 3枚目"></div>
        <figcaption class="scan-date">2020 年　○○月 ○○日 ○○時 ○○分</figcaption>
      </figure>
      <figure class="scan-card">
        <div class="scan-photo" role="img" aria-label="エコー写真 4枚目"></div>
        <figcaption class="scan-date">2020 年　○○月 ○○日 ○○時 ○○分</figcaption>
      </figure>
      <figure class="scan-card">
        <div class="scan-photo" role="img" aria-label="エコー写真 5枚目"></div>
        <figcaption class="scan-date">2020 年　○○月 ○○日 ○○時 ○○分</figcaption>
      </figure>
      <figure class="scan-card">
        <div class="scan-photo" role="img" aria-label="エコー写真 6枚目"></div>
        <figcaption class="scan-date">2020 年　○○月 ○○日 ○○時 ○○分</figcaption>
      </figure>
    </section>
  </main>
</body>
</html>
```